Brightpath Dentistry - Flyer - Modern & Eye catching campaign flyer

Need front & back side full page flyer designs for both 1) Grand opening 2) On-going campaign.

Attached the new dental office logo.
Attached our other dental clinic flyer designs for content.

Target Market(s)

Cosmetic dentistry

Industry/Entity Type

Health Care

Requirements
Must have
• decent, modern and eye catching marketing flyers.
Nice to have
• - Nice space
• - Highlight phone number
• - Highlight special features like convenient hours, call or text, for all ages, digital facility, etc
Should not have
• - Don't want to fill the flyer with too much wordings
• - Too many colors

```html
<!DOCTYPE html>
<html lang="en">
<head>
<meta charset="utf-8">
<title>Brightpath Dentistry – Grand Opening Flyer</title>
<link href="https://fonts.googleapis.com/css2?family=Marcellus&family=Montserrat:wght@400;600;700;800&display=swap" rel="stylesheet">
<style>
  :root{
    --stage:#e9eef0;
    --white:#ffffff;
    --cyan:#17b2d9;
    --teal:#0b6c82;
    --teal-deep:#0a4d61;
    --navy:#123a4a;
    --olive:#c4c78a;
    --olive-dark:#9fa35c;
  }
  *{box-sizing:border-box;margin:0;padding:0}
  html,body{width:1200px;height:1200px;overflow:hidden;background:var(--stage)}
  body{font-family:"Montserrat",sans-serif;color:var(--navy)}
  .flyer{
    position:absolute;left:160px;top:20px;width:880px;height:1160px;overflow:hidden;
    background:linear-gradient(180deg,var(--white) 0%,var(--white) 14%,#bfe8f3 32%,var(--cyan) 55%,var(--teal) 80%,var(--teal-deep) 100%);
    box-shadow:0 10px 30px rgba(0,0,0,.18);
  }
  .brand{position:absolute;top:40px;left:0;width:100%;display:flex;justify-content:center;align-items:center;gap:14px}
  .brand-dot{width:26px;height:26px;border-radius:50%;background:var(--cyan)}
  .brand-name{font-family:"Montserrat",sans-serif;font-weight:700;font-size:34px;color:var(--cyan);letter-spacing:1px;text-transform:uppercase}
  .family-photo{
    position:absolute;top:110px;left:60px;width:760px;height:470px;
    background:radial-gradient(ellipse at 50% 45%,rgba(255,255,255,.55),rgba(255,255,255,0) 70%),
               linear-gradient(180deg,rgba(255,255,255,0) 0%,rgba(160,215,235,.5) 60%,rgba(23,178,217,0) 100%);
  }
  .ribbon{position:absolute;top:560px;left:70px;width:740px;height:92px;background:var(--white);
    display:flex;align-items:center;justify-content:center;box-shadow:0 4px 10px rgba(0,0,0,.15)}
  .ribbon h1{font-family:"Marcellus",serif;font-weight:400;font-size:74px;color:var(--teal-deep);letter-spacing:2px;line-height:1}
  .ribbon-fold{position:absolute;top:652px;left:70px}
  .offers{position:absolute;top:652px;left:130px;width:620px;background:var(--teal-deep);
    border-radius:0 0 10px 10px;color:var(--white);text-align:center;padding:12px 0 10px}
  .offers-title{font-size:30px;font-weight:600;letter-spacing:1px;padding:6px 0 10px;text-transform:uppercase}
  .offer{font-size:25px;font-weight:800;text-transform:uppercase;padding:9px 0;border-top:2px solid var(--teal)}
  .call-label{position:absolute;top:868px;left:0;width:100%;text-align:center;color:var(--white);font-size:28px;font-weight:700}
  .phone-band{position:absolute;top:906px;left:150px;width:580px;height:82px;background:var(--olive);
    display:flex;align-items:center;justify-content:center;gap:22px}
  .phone-icon{width:58px;height:58px;border-radius:50%;background:var(--navy);display:flex;align-items:center;justify-content:center}
  .phone-number{font-size:60px;font-weight:800;color:var(--navy);letter-spacing:1px}
  .contact{position:absolute;top:996px;left:0;width:100%;text-align:center;color:var(--white);font-size:17px;font-weight:600;line-height:1.5}
  .contact svg{vertical-align:-3px;margin:0 6px 0 18px}
  .info-panel{position:absolute;top:1046px;left:40px;width:800px;height:114px;background:var(--white);border-radius:22px 22px 0 0;overflow:hidden;text-align:center}
  .hours{font-size:22px;font-weight:400;letter-spacing:1px;padding-top:10px;text-transform:uppercase}
  .welcome{font-size:25px;font-weight:800;text-transform:uppercase;padding-top:2px}
  .bullet{display:inline-block;width:12px;height:12px;background:var(--olive);margin:0 12px;vertical-align:2px}
  .validity{position:absolute;bottom:0;left:0;width:100%;height:36px;background:var(--olive);font-size:18px;line-height:36px;color:var(--navy)}
  .validity strong{font-weight:700}
</style>
</head>
<body>
<main class="flyer">
  <header class="brand">
    <span class="brand-dot"></span>
    <span class="brand-name">Brightpath Dentistry</span>
  </header>

  <div class="family-photo" role="img" aria-label="Smiling family of four: mother, father, son and daughter on his back"></div>

  <div class="ribbon"><h1>GRAND OPENING</h1></div>
  <svg class="ribbon-fold" width="60" height="30" viewBox="0 0 60 30"><polygon points="0,0 60,0 60,30" fill="#c9d3d6"/></svg>

  <section class="offers">
    <p class="offers-title">Special Opening Offers:</p>
    <p class="offer">Free Kids Dental Screening</p>
    <p class="offer">$25 Adults Dental Screening</p>
    <p class="offer">15% Off on Treatment Plan</p>
  </section>

  <p class="call-label">Call or Text Us Now</p>
  <div class="phone-band">
    <span class="phone-icon">
      <svg width="30" height="30" viewBox="0 0 24 24"><path fill="#c4c78a" d="M6.6 10.8a15.1 15.1 0 0 0 6.6 6.6l2.2-2.2a1 1 0 0 1 1-.25 11.4 11.4 0 0 0 3.6.57 1 1 0 0 1 1 1V20a1 1 0 0 1-1 1A17 17 0 0 1 3 4a1 1 0 0 1 1-1h3.5a1 1 0 0 1 1 1c0 1.25.2 2.45.57 3.57a1 1 0 0 1-.25 1z"/></svg>
    </span>
    <span class="phone-number">555.014.2276</span>
  </div>

  <div class="contact">
    <p><svg width="16" height="16" viewBox="0 0 24 24"><circle cx="12" cy="12" r="10" fill="none" stroke="#fff" stroke-width="2"/><path d="M2 12h20M12 2c3 3 3 17 0 20M12 2c-3 3-3 17 0 20" fill="none" stroke="#fff" stroke-width="1.5"/></svg>www.BrightpathDental.com<svg width="16" height="16" viewBox="0 0 24 24"><rect x="3" y="6" width="18" height="13" fill="none" stroke="#fff" stroke-width="2"/><path d="M3 6l9 7 9-7" fill="none" stroke="#fff" stroke-width="2"/></svg>info@BrightpathDental.com</p>
    <p><svg width="16" height="16" viewBox="0 0 24 24"><path d="M12 2a7 7 0 0 0-7 7c0 5 7 13 7 13s7-8 7-13a7 7 0 0 0-7-7z" fill="none" stroke="#fff" stroke-width="2"/><circle cx="12" cy="9" r="2.5" fill="#fff"/></svg>412 Maple Row, Fairview PA 19000</p>
  </div>

  <footer class="info-panel">
    <p class="hours"><span class="bullet"></span>Convenient Evening &amp; Saturday Hours<span class="bullet"></span></p>
    <p class="welcome"><span class="bullet"></span>New Patients Are Welcome!<span class="bullet"></span></p>
    <p class="validity">Opening special offers valid until June 15, 2019 <strong>by appointment only</strong></p>
  </footer>
</main>
</body>
</html>
```